Geschäftspapiere für telefonische Kaltakquise in der Immobilienbranche
Zielgruppe
Wir produzieren via telefonischer Kaltakquise Leads und Termine für Immobilienmakler
Aufgabenstellung
Gute Frage, es soll schön aussehen und Kunden begeistern.

```html
<!DOCTYPE html>
<html lang="de">
<head>
<meta charset="utf-8">
<title>Veltaro24 Briefpapier</title>
<link rel="stylesheet" href="https://fonts.googleapis.com/css2?family=Open+Sans:wght@400;600;700&display=swap">
<style>
  :root {
    --bg: #eff1f5;
    --paper: #ffffff;
    --magenta: #d40f6f;
    --violet: #8a3aa0;
    --blue: #3a6ad6;
    --purple-text: #6a2f9a;
    --grey-text: #8a8a8a;
    --logo-grey: #8d8d8d;
    --rule: #7a3aa6;
  }
  * { margin: 0; padding: 0; box-sizing: border-box; }
  html, body { width: 1200px; height: 1200px; overflow: hidden; background: var(--bg); }
  body { position: relative; font-family: "Open Sans", Arial, sans-serif; }

  .letterhead {
    position: absolute; left: 229px; top: 70px; width: 744px; height: 1053px;
    background: var(--paper);
    box-shadow: 14px 16px 26px rgba(60, 70, 90, 0.28);
  }
  .top-band {
    position: absolute; left: 0; top: 0; width: 100%; height: 16px;
    background: linear-gradient(90deg, var(--magenta), var(--violet) 55%, var(--blue));
  }

  .brand {
    position: absolute; display: flex; align-items: center;
    color: var(--logo-grey); font-weight: 600; letter-spacing: 2px;
  }
  .brand-dot { border-radius: 50%; background: var(--magenta); flex: none; }
  .brand--header { left: 52px; top: 56px; font-size: 40px; }
  .brand--header .brand-dot { width: 42px; height: 42px; margin-right: 10px; }
  .brand--footer { right: 42px; top: 982px; font-size: 21px; letter-spacing: 1.2px; }
  .brand--footer .brand-dot { width: 24px; height: 24px; margin-right: 6px; }

  .contact {
    position: absolute; left: 571px; top: 50px; padding-left: 8px;
    border-left: 1.5px solid var(--rule);
    font-size: 10.5px; line-height: 15px; color: var(--grey-text);
  }
  .contact-address { margin-bottom: 9px; }
  .contact-line { display: flex; align-items: center; }
  .contact-line svg { width: 9px; height: 9px; margin-right: 8px; fill: var(--violet); flex: none; }

  .bank {
    position: absolute; left: 52px; top: 942px; padding-left: 8px;
    border-left: 1.5px solid var(--rule);
    font-size: 11px; line-height: 14.5px; color: var(--grey-text);
  }
  .bank-title { color: var(--purple-text); font-weight: 700; margin-bottom: 6px; }
  .tax-id {
    position: absolute; left: 250px; top: 948px; padding-left: 7px;
    border-left: 1.5px solid var(--rule);
    font-size: 10.5px; line-height: 11px; color: var(--grey-text);
  }

  .bottom-band { position: absolute; left: 0; bottom: 0; width: 744px; height: 38px; }
</style>
</head>
<body>
  <main class="letterhead">
    <div class="top-band"></div>

    <div class="brand brand--header"><span class="brand-dot"></span>VELTARO24</div>

    <address class="contact" style="font-style:normal">
      <div class="contact-address">Address address<br>41414 address</div>
      <div class="contact-line"><svg viewBox="0 0 10 10"><path d="M1 3.5C1 2 3 1.5 5 1.5S9 2 9 3.5V4.5H7V3.5H3V4.5H1ZM2 5.5H8V8.5H2Z"/></svg>021XX 15XXXXX</div>
      <div class="contact-line"><svg viewBox="0 0 10 10"><path d="M2.5 1H7.5V3.5H2.5ZM1 4H9V7.5H7.5V9H2.5V7.5H1ZM3.5 6.5V8H6.5V6.5Z"/></svg>0322 XXX XX XXX</div>
      <div class="contact-line"><svg viewBox="0 0 10 10"><path d="M1 2.5H9V7.5H1ZM1.8 3.2L5 5.6L8.2 3.2V3.2H1.8Z"/></svg>kontakt@veltaro24.de</div>
      <div class="contact-line"><svg viewBox="0 0 10 10"><path d="M5 1A4 4 0 1 0 5 9A4 4 0 1 0 5 1ZM5 1.9A3.1 3.1 0 0 1 8.1 4.6H1.9A3.1 3.1 0 0 1 5 1.9ZM1.9 5.4H8.1A3.1 3.1 0 0 1 1.9 5.4Z" fill-rule="evenodd"/></svg>www.veltaro24.de</div>
    </address>

    <div class="bank">
      <div class="bank-title">Bankverbindung:</div>
      Veltaro24<br>
      IBAN: DEXX XXXX XXXX XXXX XXXX X<br>
      BIC: XXXXXXXX<br>
      Nordhafen Bank
    </div>
    <div class="tax-id">USt-ID-Nr. DEXXXXXXX</div>

    <div class="brand brand--footer"><span class="brand-dot"></span>VELTARO24</div>

    <svg class="bottom-band" viewBox="0 0 744 38" preserveAspectRatio="none" aria-hidden="true">
      <defs>
        <linearGradient id="band-gradient" x1="0" x2="1" y1="0" y2="0">
          <stop offset="0" stop-color="#d40f6f"/>
          <stop offset="0.55" stop-color="#8a3aa0"/>
          <stop offset="1" stop-color="#3a6ad6"/>
        </linearGradient>
        <linearGradient id="swoosh-gradient" x1="499" x2="744" y1="0" y2="0" gradientUnits="userSpaceOnUse">
          <stop offset="0" stop-color="#d40f6f"/>
          <stop offset="0.5" stop-color="#8a3aa0"/>
          <stop offset="1" stop-color="#3a6ad6"/>
        </linearGradient>
      </defs>
      <rect x="0" y="15" width="744" height="23" fill="url(#band-gradient)"/>
      <path d="M499 5H744V20H552C530 20 520 14 499 5Z" fill="url(#swoosh-gradient)"/>
      <path d="M499 5C522 17 532 24 554 24H744V16H554C534 16 522 12 499 5Z" fill="#ffffff"/>
    </svg>
  </main>
</body>
</html>
```